Graphics for website image slider

We need 4 banners for website:

We provide software development services to very small to large Businesses. The focus of these 4 banners is to portray the four steps approach to our consulting process: Assess, Analyse, Plan and Deploy

Currently we have the following on our website:
http://www.virelanq.com

We are redesigning the website and want to use 4 sliding graphics to portray the same thing, and the new site is being designed here:
http://www.virelanqonline.com/virelanq

You can use stock photos for each banner or your own creativity.

The images should be 1140px wide and about 420px High.
Updates

You can use any modern font such as google font. Not just curly fonts!

Reason: Not yet able to select the final design.

I have updated the colors and how they are supposed to flow because I noticed that some designs did not follow that (We are consultants and really want to understand our process in a powerful way):

ASSESS: Orange color (1st or 5th color above)

ANALYSE: Yellow (2nd or 6th color above)

PLAN: Green (3rd or 7th color above)

DEPLOY: Blue (4th or 8th color above)

=================================================

Some designers also made mistakes in typing the text (Please copy and paste from below):

ASSESS

We gather information and data

to identify and delineate

your central and most pressing business and IT issues.

ANALYSE

We show you exactly where you are in terms of IT maturity

using our optimization tools.

We then build an IT roadmap to help you get to the next level.

PLAN:

We identify the IT products and processes necessary to implement the solution.

We then create a detailed plan of action and technical specifications.

DEPLOY

Finally, we utilize industry best practices and repeatable development and

deployment methods to ensure efficiency and high quality results

that satisfy and bring improvement within budget and timeline.

                                   

Target Market(s)

http://www.virelanq.com

Industry/Entity Type

Software

Font styles to use
Sans Serif
Other font styles liked:
• Any other modern font (No curly fonts)

Colors
fee18a
fbf289
cadf82
86cae6
f78f20
ffc214
9aca3c
0692cd

Requirements
Must have
• Graphic should convey the message for each process

```html
<!DOCTYPE html>
<html lang="en">
<head>
<meta charset="utf-8">
<title>Consulting Process – Assess, Analyse, Plan, Deploy</title>
<link rel="stylesheet" href="https://fonts.googleapis.com/css2?family=Play:wght@400;700&display=swap">
<style>
  :root {
    --assess: #f78f20;
    --assess-soft: #fee18a;
    --analyse: #ffc214;
    --analyse-soft: #fbf289;
    --plan: #9aca3c;
    --plan-soft: #cadf82;
    --plan-title: #8fae23;
    --deploy: #0692cd;
    --deploy-soft: #86cae6;
    --ink: #111111;
    --divider: #8a8a8a;
    --step-idle: rgba(255,255,255,0.38);
    --step-label-idle: rgba(255,255,255,0.85);
  }
  * { margin: 0; padding: 0; box-sizing: border-box; }
  html, body { width: 811px; height: 1200px; overflow: hidden; background: var(--divider); }
  .slider-stack {
    width: 811px; height: 1200px;
    display: flex; flex-direction: column; gap: 4px;
    font-family: 'Play', sans-serif;
  }
  .banner {
    position: relative; height: 297px; overflow: hidden;
  }
  .banner--assess {
    background: radial-gradient(ellipse 70% 90% at 38% 40%, #fffbe8 0%, var(--assess-soft) 45%, #fbb24a 85%, var(--assess) 110%);
  }
  .banner--analyse {
    background: radial-gradient(ellipse 70% 90% at 40% 40%, #fffef0 0%, var(--analyse-soft) 50%, #fcd94a 90%, var(--analyse) 115%);
  }
  .banner--plan {
    background: radial-gradient(ellipse 70% 90% at 45% 35%, #fbfde8 0%, #e8f2a8 35%, var(--plan-soft) 65%, var(--plan) 115%);
  }
  .banner--deploy {
    background: radial-gradient(ellipse 70% 90% at 45% 40%, #ffffff 0%, #e4f3fa 40%, var(--deploy-soft) 85%, #4fb0dc 120%);
  }
  .banner__sweep {
    position: absolute; left: -80px; top: 150px; width: 1000px; height: 260px;
    border-radius: 50%; border-top: 18px solid rgba(255,255,255,0.35);
    transform: rotate(-10deg);
  }
  .banner__title {
    position: absolute; left: 38px; top: 22px;
    font-size: 24px; font-weight: 700; letter-spacing: 0.2px;
  }
  .banner--assess .banner__title { color: var(--assess); }
  .banner--analyse .banner__title { color: var(--analyse); }
  .banner--plan .banner__title { color: var(--plan-title); }
  .banner--deploy .banner__title { color: var(--deploy); }
  .banner__copy {
    position: absolute; left: 38px; top: 64px;
    font-size: 17.5px; line-height: 23.5px; color: var(--ink); font-weight: 700;
  }
  .banner__art {
    position: absolute; left: 590px; top: 50px; width: 200px; height: 190px;
    border-radius: 40%;
  }
  .banner--assess .banner__art { background: radial-gradient(circle, #f7a21f 0%, rgba(247,143,32,0.5) 55%, rgba(247,143,32,0) 75%); }
  .banner--analyse .banner__art { background: radial-gradient(circle, #e9e9e9 0%, rgba(220,220,220,0.6) 55%, rgba(220,220,220,0) 75%); }
  .banner--plan .banner__art { left: 610px; top: 40px; width: 170px; height: 220px; background: radial-gradient(circle, #f07a12 0%, rgba(240,122,18,0.5) 55%, rgba(240,122,18,0) 75%); }
  .banner--deploy .banner__art { left: 575px; top: 50px; width: 215px; height: 210px; background: radial-gradient(circle, #2ba3d6 0%, rgba(43,163,214,0.5) 55%, rgba(43,163,214,0) 75%); }
  .process-steps {
    position: absolute; left: 14px; top: 240px; width: 560px; height: 44px;
  }
  .process-steps text {
    font-family: 'Play', sans-serif; font-size: 13px; font-weight: 700;
    text-anchor: middle; fill: var(--step-label-idle);
  }
  .process-steps .step--active text { fill: #ffffff; }
  .step__shape { fill: var(--step-idle); }
  .step__tail { fill: none; stroke: var(--step-idle); stroke-width: 5; }
  .banner--assess .step--active .step__shape { fill: var(--assess); }
  .banner--assess .step--active .step__tail { stroke: var(--assess); }
  .banner--analyse .step--active .step__shape { fill: var(--analyse); }
  .banner--analyse .step--active .step__tail { stroke: var(--analyse); }
  .banner--plan .step--active .step__shape { fill: var(--plan); }
  .banner--plan .step--active .step__tail { stroke: var(--plan); }
  .banner--deploy .step--active .step__shape { fill: var(--deploy); }
  .banner--deploy .step--active .step__tail { stroke: var(--deploy); }
</style>
</head>
<body>
<main class="slider-stack">

  <section class="banner banner--assess">
    <div class="banner__sweep"></div>
    <h2 class="banner__title">Assess</h2>
    <p class="banner__copy">We gather information and data to identify<br>and delineate your central and most pressing<br>business and IT issues.</p>
    <div class="banner__art" role="img" aria-label="Orange figure examining with a magnifying glass"></div>
    <svg class="process-steps" viewBox="0 0 560 44">
      <g class="step step--active"><polygon class="step__shape" points="2,2 110,2 128,22 110,42 2,42"/><polyline class="step__tail" points="114,4 132,22 114,40"/><polyline class="step__tail" points="124,4 142,22 124,40"/><text x="60" y="27">ASSESS</text></g>
      <g class="step"><polygon class="step__shape" points="134,2 241,2 259,22 241,42 134,42 152,22"/><polyline class="step__tail" points="245,4 263,22 245,40"/><polyline class="step__tail" points="255,4 273,22 255,40"/><text x="198" y="27">ANALYSE</text></g>
      <g class="step"><polygon class="step__shape" points="266,2 372,2 390,22 372,42 266,42 284,22"/><polyline class="step__tail" points="376,4 394,22 376,40"/><polyline class="step__tail" points="386,4 404,22 386,40"/><text x="322" y="27">PLAN</text></g>
      <g class="step"><polygon class="step__shape" points="397,2 503,2 521,22 503,42 397,42 415,22"/><polyline class="step__tail" points="507,4 525,22 507,40"/><polyline class="step__tail" points="517,4 535,22 517,40"/><text x="452" y="27">DEPLOY</text></g>
    </svg>
  </section>

  <section class="banner banner--analyse">
    <div class="banner__sweep"></div>
    <h2 class="banner__title">Analyse</h2>
    <p class="banner__copy">We show you exactly where you are in terms of<br>IT maturity using our optimization tools.<br>We then build an IT roadmap to help you get<br>to the next level.</p>
    <div class="banner__art" role="img" aria-label="White figure holding a large magnifying glass"></div>
    <svg class="process-steps" viewBox="0 0 560 44">
      <g class="step"><polygon class="step__shape" points="2,2 110,2 128,22 110,42 2,42"/><polyline class="step__tail" points="114,4 132,22 114,40"/><polyline class="step__tail" points="124,4 142,22 124,40"/><text x="60" y="27">ASSESS</text></g>
      <g class="step step--active"><polygon class="step__shape" points="134,2 241,2 259,22 241,42 134,42 152,22"/><polyline class="step__tail" points="245,4 263,22 245,40"/><polyline class="step__tail" points="255,4 273,22 255,40"/><text x="198" y="27">ANALYSE</text></g>
      <g class="step"><polygon class="step__shape" points="266,2 372,2 390,22 372,42 266,42 284,22"/><polyline class="step__tail" points="376,4 394,22 376,40"/><polyline class="step__tail" points="386,4 404,22 386,40"/><text x="322" y="27">PLAN</text></g>
      <g class="step"><polygon class="step__shape" points="397,2 503,2 521,22 503,42 397,42 415,22"/><polyline class="step__tail" points="507,4 525,22 507,40"/><polyline class="step__tail" points="517,4 535,22 517,40"/><text x="452" y="27">DEPLOY</text></g>
    </svg>
  </section>

  <section class="banner banner--plan">
    <div class="banner__sweep"></div>
    <h2 class="banner__title">Plan</h2>
    <p class="banner__copy">We identify the IT products and processes<br>necessary to implement the solution.<br>We then create a detailed plan of action<br>and technical specifications.</p>
    <div class="banner__art" role="img" aria-label="Orange figure with glasses holding a clipboard"></div>
    <svg class="process-steps" viewBox="0 0 560 44">
      <g class="step"><polygon class="step__shape" points="2,2 110,2 128,22 110,42 2,42"/><polyline class="step__tail" points="114,4 132,22 114,40"/><polyline class="step__tail" points="124,4 142,22 124,40"/><text x="60" y="27">ASSESS</text></g>
      <g class="step"><polygon class="step__shape" points="134,2 241,2 259,22 241,42 134,42 152,22"/><polyline class="step__tail" points="245,4 263,22 245,40"/><polyline class="step__tail" points="255,4 273,22 255,40"/><text x="198" y="27">ANALYSE</text></g>
      <g class="step step--active"><polygon class="step__shape" points="266,2 372,2 390,22 372,42 266,42 284,22"/><polyline class="step__tail" points="376,4 394,22 376,40"/><polyline class="step__tail" points="386,4 404,22 386,40"/><text x="322" y="27">PLAN</text></g>
      <g class="step"><polygon class="step__shape" points="397,2 503,2 521,22 503,42 397,42 415,22"/><polyline class="step__tail" points="507,4 525,22 507,40"/><polyline class="step__tail" points="517,4 535,22 517,40"/><text x="452" y="27">DEPLOY</text></g>
    </svg>
  </section>

  <section class="banner banner--deploy">
    <div class="banner__sweep"></div>
    <h2 class="banner__title">Deploy</h2>
    <p class="banner__copy">Finally, we utilize industry best practices and<br>repeatable development &amp; deployment methods<br>to ensure efficiency and high quality results<br>that satisfy and bring improvement.</p>
    <div class="banner__art" role="img" aria-label="Two interlocking blue gears"></div>
    <svg class="process-steps" viewBox="0 0 560 44">
      <g class="step"><polygon class="step__shape" points="2,2 110,2 128,22 110,42 2,42"/><polyline class="step__tail" points="114,4 132,22 114,40"/><polyline class="step__tail" points="124,4 142,22 124,40"/><text x="60" y="27">ASSESS</text></g>
      <g class="step"><polygon class="step__shape" points="134,2 241,2 259,22 241,42 134,42 152,22"/><polyline class="step__tail" points="245,4 263,22 245,40"/><polyline class="step__tail" points="255,4 273,22 255,40"/><text x="198" y="27">ANALYSE</text></g>
      <g class="step"><polygon class="step__shape" points="266,2 372,2 390,22 372,42 266,42 284,22"/><polyline class="step__tail" points="376,4 394,22 376,40"/><polyline class="step__tail" points="386,4 404,22 386,40"/><text x="322" y="27">PLAN</text></g>
      <g class="step step--active"><polygon class="step__shape" points="397,2 503,2 521,22 503,42 397,42 415,22"/><polyline class="step__tail" points="507,4 525,22 507,40"/><polyline class="step__tail" points="517,4 535,22 517,40"/><text x="452" y="27">DEPLOY</text></g>
    </svg>
  </section>

</main>
</body>
</html>
```